ZEPRILO.COM is a premium domain sales company. Our competitors are companies like vastplots.example, getparcels.example, peerwords.example. Our current site is at www.zeprilos.example.

We want to have the ability to search for domains, to highlight special offers and have some testimonials on the index page.

The logo for the site is attached.

Please be sure that the order form fits on the screen without scrolling the page. I want the entire form, including the submit button to fit without any page scrolling.

Delivered product - INDEX PAGE, ORDER FORM AND CONTENT PAGE PSDs.

Target Market(s)

Small to Medium business professionals

Industry/Entity Type

It Company

Requirements
Must have
• 1. List of domains for sale
2. Simple search box with button to run the search
3. link for advanced search
4. testimonial area. Note - this can be a small box where a different testimonial is displayed on each page load.
Nice to have
• Would like the site to have some white space. Don't want a heavily packed website. Give it an "airy" feel.

```html
<!DOCTYPE html>
<html lang="en">
<head>
<meta charset="utf-8">
<title>ZEPRILO.COM — Premium Domains</title>
<link href="https://fonts.googleapis.com/css2?family=Arimo:wght@400;700&family=Raleway:wght@200;300&display=swap" rel="stylesheet">
<style>
:root{
  --green:#1b7a3c;
  --blue:#1e5fa6;
  --navy:#1a4f8c;
  --band:#cdd9e8;
  --band-edge:#a9bcd6;
  --text:#6d6d6d;
  --dark:#3d3d3d;
  --line:#e4e4e4;
  --panel:#f1f1f1;
  --page:#ffffff;
  --foot:#f2f2f2;
  --bar:#d8dee8;
}
*{box-sizing:border-box;margin:0;padding:0}
html,body{width:669px;height:1200px;overflow:hidden;background:var(--page)}
body{position:relative;font-family:"Arimo",Arial,sans-serif;color:var(--text);font-size:7px}
a{color:inherit;text-decoration:none}
.abs{position:absolute}

/* top nav */
.topnav{left:66px;top:11px;height:20px;display:flex;border:1px solid #d0d0d0;border-radius:3px;background:linear-gradient(#fafafa,#e9e9e9)}
.topnav a{display:flex;align-items:center;padding:0 12px;font-size:7px;color:var(--dark);border-left:1px solid #d6d6d6}
.topnav a:first-child{border-left:0;padding:0 10px}
.help{right:66px;top:10px;text-align:right}
.help .q{font-size:10px;font-weight:700;color:var(--green)}
.help .q span{font-size:6.5px;font-weight:400;color:#8a8a8a}
.help .tel{font-size:9.5px;color:var(--green);margin-top:3px}

/* search band */
.searchband{left:66px;top:39px;width:537px;height:61px;background:linear-gradient(#dae3ef,var(--band));border:1px solid var(--band-edge);border-radius:4px 4px 0 0}
.logo{position:absolute;left:13px;top:23px;font-size:13px;font-weight:700;color:var(--green);letter-spacing:-0.2px;white-space:nowrap}
.search-label{position:absolute;left:125px;top:27px;font-family:"Raleway",sans-serif;font-weight:300;font-size:8.5px;color:#6b7480;letter-spacing:.1px;white-space:nowrap}
.search-field{position:absolute;left:253px;top:21px;width:243px;height:20px;background:#fff;border:1px solid #c9c9c9;font-size:6px;color:#666;padding:6px 6px;white-space:nowrap;overflow:hidden}
.search-btn{position:absolute;left:504px;top:21px;width:20px;height:20px;background:var(--navy);border-radius:2px}
.adv{position:absolute;left:254px;top:50px;font-size:6px;color:var(--green);text-decoration:underline}
.adv::before{content:"";position:absolute;left:-10px;top:1px;border-left:4px solid var(--green);border-top:3px solid transparent;border-bottom:3px solid transparent}

/* hero */
.hero{left:66px;top:100px;width:537px;height:166px;background:linear-gradient(#fbfbfb,#f1f1f1)}
.hero-art{position:absolute;left:26px;top:30px;width:322px;height:100px;background:radial-gradient(ellipse at 45% 50%,#c7d6ea 0,#e9edf2 45%,rgba(241,241,241,0) 70%)}
.hero-copy{position:absolute;left:331px;top:44px;width:180px}
.hero-copy h1{font-size:9.5px;line-height:12px;font-weight:700;color:var(--navy)}
.hero-copy h1 span{color:var(--green)}
.hero-copy p{margin-top:10px;font-size:8.5px;line-height:10.5px;color:#8a8a8a}
.dots{left:312px;top:271px;display:flex;gap:3px}
.dots i{width:6px;height:6px;border-radius:50%;background:#c9c9c9}
.dots i.on{background:var(--green)}

/* features */
.features{left:66px;top:282px;width:537px;height:55px;background:linear-gradient(#fff,#f3f3f3)}
.feature{position:absolute;top:0;display:flex;align-items:center;height:55px;font-size:7.5px;font-weight:700;color:#7a7a7a;white-space:nowrap}
.feature .ico{width:38px;height:38px;border-radius:50%;background:radial-gradient(#9a9a9a,#d8d8d8 70%);margin-right:10px}

/* featured table */
.panel-head{height:25px;background:var(--panel);font-size:8px;color:var(--navy);padding:9px 13px}
.featured{left:66px;top:349px;width:336px}
.cols{display:flex;padding:13px 13px 0;font-size:7px;color:var(--green);height:32px}
.c1{width:107px}.c2{width:99px}.c3{width:82px}
.row{display:flex;align-items:center;height:41.5px;padding:0 0 0 13px;border-bottom:1px solid var(--line);font-size:7px;color:#8a8a8a;background:linear-gradient(#fff 70%,#f7f7f7)}
.buy{width:40px;height:16px;border:1px solid #cfcfcf;border-radius:3px;background:linear-gradient(#fdfdfd,#e6e6e6);font-size:6.5px;color:#777;display:flex;align-items:center;justify-content:center;white-space:nowrap}
.pager{left:275px;top:828px;display:flex;gap:4px;align-items:center}
.pager span{width:14px;height:13px;border:1px solid #d5d5d5;background:#f4f4f4;font-size:6px;color:#555;display:flex;align-items:center;justify-content:center}
.pager span.on{background:#8e8e8e;color:#fff;border-color:#8e8e8e}
.pager em{font-style:normal;font-size:7.5px;color:#888;margin-left:8px}

/* categories */
.cats{left:420px;top:349px;width:182px}
.cats ul{list-style:none;margin-top:14px}
.cats li{display:flex;justify-content:space-between;height:14px;padding:3px 0 0 14px;border-bottom:1px dashed #9a9a9a;font-size:6.3px;color:#8a8a8a}
.cats li.hl{background:#ececec}

/* testimonial */
.divider{left:66px;top:866px;width:537px;border-top:1px solid #e6e6e6}
.say-title{left:0;width:669px;top:881px;text-align:center;font-family:"Raleway",sans-serif;font-weight:200;font-size:17px;color:#555}
.avatar{left:309px;top:908px;width:48px;height:48px;border-radius:50%;background:radial-gradient(#e8e8e8,#c2c2c2);border:2px solid #eee}
.arrow{top:925px}
.who{left:0;width:669px;top:971px;text-align:center;font-size:7px;color:#333}
.who span{color:var(--blue)}
.quote{left:105px;width:460px;top:984px;text-align:center;font-size:6.5px;line-height:10px;color:#a5a5a5}
.qm{font-family:Georgia,serif;font-size:40px;color:#e4e4e4;line-height:1}
.posted{left:0;width:669px;top:1014px;text-align:center;font-size:6px;color:var(--blue)}

/* footer */
.footer{left:0;top:1048px;width:669px;height:129px;background:var(--foot)}
.fcol{position:absolute;top:19px}
.fcol h4{font-size:7.5px;font-weight:400;color:var(--blue);margin-bottom:9px}
.fcol li{list-style:none;font-size:6.3px;color:#888;height:10.5px;white-space:nowrap}
.social li{display:flex;align-items:center;height:17.5px}
.social i{width:11px;height:11px;background:#7f8fa6;border-radius:2px;margin-right:12px}
.social b{font-weight:400;color:#444;margin-left:3px}
.addr{font-size:6.3px;line-height:8.2px;color:#888}
.bottombar{left:0;top:1177px;width:669px;height:23px;background:var(--bar);text-align:center;font-size:6.5px;color:#666;padding-top:8px}
.bottombar span{color:var(--blue)}
.live{right:0;bottom:0}
</style>
</head>
<body>

<nav class="topnav abs">
  <a href="#" aria-label="Home"><svg width="11" height="9" viewBox="0 0 11 9"><path d="M1 4.5 5.5 1 10 4.5M2.5 3.8V8.5h6V3.8" fill="none" stroke="#aaa" stroke-width="1"/></svg></a>
  <a href="#">Catgories</a><a href="#">FAQs</a><a href="#">About us</a><a href="#">Contact us</a>
</nav>
<div class="help abs">
  <div class="q">Questions? <span>We're here to help! Call today:</span></div>
  <div class="tel">+100 555 0142</div>
</div>

<header class="searchband abs">
  <div class="logo">ZEPRILO.COM</div>
  <div class="search-label">SEARCH YOUR DOMAIN NAME</div>
  <div class="search-field">Start your search by entering the first character of the domain name.</div>
  <div class="search-btn"><svg width="20" height="20" viewBox="0 0 20 20"><circle cx="8.5" cy="8.5" r="4" fill="none" stroke="#fff" stroke-width="2"/><path d="M11.5 11.5 15 15" stroke="#fff" stroke-width="2.4" stroke-linecap="round"/></svg></div>
  <a class="adv" href="#">Advanced Search</a>
</header>

<section class="hero abs">
  <div class="hero-art" role="img" aria-label="Illustration of a blue web globe over a sketched town landscape"></div>
  <div class="hero-copy">
    <h1>LOOKING FOR &nbsp;A DOMAIN NAME?<br><span>FIND A SUITABLE NAME EASILY!</span></h1>
    <p>Lorem ipsum dolor sit amet, consectetur piscing elit. Ut rhoncus ornare nisi non msan. Etiam sed nulla at ante sollicitudin quam. Phasellus feugiat lacus</p>
  </div>
</section>
<div class="dots abs"><i></i><i></i><i class="on"></i><i></i><i></i></div>

<section class="features abs">
  <div class="feature" style="left:20px"><div class="ico" role="img" aria-label="Thumbs-up guarantee badge"></div>100% Satisfaction Guarantee</div>
  <div class="feature" style="left:213px"><div class="ico" role="img" aria-label="Globe with magnifier"></div>World Class Customer Service</div>
  <div class="feature" style="left:410px"><div class="ico" role="img" aria-label="Padlock"></div>Trusted and Secure</div>
</section>

<section class="featured abs">
  <div class="panel-head">Featured Domains</div>
  <div class="cols"><div class="c1">Domain</div><div class="c2">Category</div><div class="c3">Price</div></div>
  <div class="row"><div class="c1">quorvalin.com</div><div class="c2">Health</div><div class="c3">$8700.00</div><div class="buy">BUY NOW!</div></div>
  <div class="row"><div class="c1">trailpocket.com</div><div class="c2">Sports</div><div class="c3">$5000.00</div><div class="buy">BUY NOW!</div></div>
  <div class="row"><div class="c1">autoclassiq.com</div><div class="c2">Vehicles</div><div class="c3">$100.00</div><div class="buy">BUY NOW!</div></div>
  <div class="row"><div class="c1">newvantrix.com</div><div class="c2">Vehicles</div><div class="c3">$100.00</div><div class="buy">BUY NOW!</div></div>
  <div class="row"><div class="c1">descarmelody.com</div><div class="c2">Other</div><div class="c3">$4397.00</div><div class="buy">BUY NOW!</div></div>
  <div class="row"><div class="c1">allthenests.com</div><div class="c2">Real Estate</div><div class="c3">$4397.00</div><div class="buy">BUY NOW!</div></div>
  <div class="row"><div class="c1">news-q.com</div><div class="c2">Media</div><div class="c3">$197.00</div><div class="buy">BUY NOW!</div></div>
  <div class="row"><div class="c1">procesosnorte.com</div><div class="c2">Law</div><div class="c3">$197.00</div><div class="buy">BUY NOW!</div></div>
  <div class="row"><div class="c1">clearledgerhub.com</div><div class="c2">Finance</div><div class="c3">$300.00</div><div class="buy">BUY NOW!</div></div>
  <div class="row"><div class="c1">ohzap.com</div><div class="c2">Other</div><div class="c3">$211.00</div><div class="buy">BUY NOW!</div></div>
</section>
<div class="pager abs"><span class="on">1</span><span>2</span><span>3</span><span>4</span><span>5</span><em>View More</em></div>

<aside class="cats abs">
  <div class="panel-head">Domains Categories</div>
  <ul>
    <li>Art<span>Review</span></li><li class="hl">Business<span>Review</span></li><li>Education<span>Review</span></li><li>Electronics<span>Review</span></li><li>Employment<span>Review</span></li><li>Entertainment<span>Review</span></li><li>Finance<span>Review</span></li><li>Food &nbsp;Water<span>Review</span></li><li>Games<span>Review</span></li><li>Government<span>Review</span></li><li>Health<span>Review</span></li><li>Home<span>Review</span></li><li>International<span>Review</span></li><li>Internet<span>Review</span></li><li>Kids<span>Review</span></li><li>Kids and Family<span>Review</span></li><li>Law<span>Review</span></li><li>Local<span>Review</span></li><li>Media<span>Review</span></li><li>News<span>Review</span></li><li>Other<span>Review</span></li><li>Real Estate<span>Review</span></li><li>Recreation<span>Review</span></li><li>Reference<span>Review</span></li><li>Science<span>Review</span></li><li>Science and World<span>Review</span></li><li>Services<span>Review</span></li><li>Shopping<span>Review</span></li><li>Society<span>Review</span></li><li>Sports<span>Review</span></li><li>Technology<span>Review</span></li><li>Travel<span>Review</span></li><li>Vehicles<span>Review</span></li>
  </ul>
</aside>

<div class="divider abs"></div>
<h2 class="say-title abs">What our clients say!</h2>
<svg class="arrow abs" style="left:284px" width="8" height="14" viewBox="0 0 8 14"><path d="M7 1 1 7l6 6" fill="none" stroke="#888" stroke-width="1.2"/></svg>
<div class="avatar abs" role="img" aria-label="Client portrait placeholder"></div>
<svg class="arrow abs" style="left:374px" width="8" height="14" viewBox="0 0 8 14"><path d="M1 1l6 6-6 6" fill="none" stroke="#888" stroke-width="1.2"/></svg>
<div class="who abs">DANA WHITLOCK <span>MANAGER</span></div>
<div class="qm abs" style="left:82px;top:968px">&ldquo;</div>
<p class="quote abs">Lorem ipsum dolor sit amet consectetur adipiscing elit. Curabitur lorem in design Morbi nec in. Curabitur laoreet nisl lorem design dolor gamin nullam ductus gojus. Vurabi laoreet nisl lorem in design Morbi nec in. Curabitur laoreet nisl lorem design desirus gamin facitus gojus.</p>
<div class="posted abs">DATE: OCTOBER 25, 2012 POSTED BY: ADMIN 12 COMMENTS</div>
<div class="qm abs" style="left:422px;top:1008px">&rdquo;</div>

<footer class="footer abs">
  <div class="fcol" style="left:66px"><h4>LINKS</h4><ul><li>Home</li><li>Categories</li><li>FAQs</li><li>About us</li><li>Contact us</li><li>Universal Terms</li><li>Refund Policy</li><li>Privacy Policy</li></ul></div>
  <div class="fcol" style="left:150px"><h4>DOMAINS FOR SALE</h4><ul><li>Newest Domains</li><li>Elite Domains</li><li>Cheap Domains</li></ul></div>
  <div class="fcol" style="left:271px"><h4>DELETING DOMAINS</h4><ul><li>Traffic score</li><li>Domain rank</li><li>Popularity score</li><li>US based traffic percent</li></ul></div>
  <div class="fcol social" style="left:397px"><h4>GET CONNECTED ON</h4><ul><li><i></i>Like us on<b>Pagewall</b></li><li><i></i>Follow us on<b>Chirper</b></li><li><i></i>Contact us on<b>Worklink</b></li><li><i></i>Watch us on<b>Clipstream</b></li></ul></div>
  <div class="fcol" style="left:537px"><h4>CONTACT</h4><p class="addr">(c) 2013 Zeprilo, Inc.<br>48 Harbor Lane<br>Suite 12<br>Fairview, OR 97024<br>United States<br><br>+1 555.010.2840</p></div>
</footer>
<div class="bottombar abs">Copyright &copy; 2013 <span>Zeprilo.com</span></div>

<svg class="live abs" width="104" height="76" viewBox="0 0 104 76" role="img" aria-label="Live support (off line)">
  <path d="M104 0V76H0Z" fill="#1f8a3e"/>
  <text x="40" y="71" transform="rotate(-36 40 71)" font-family="Arimo, Arial, sans-serif" font-size="5.5" fill="#fff">LIVE SUPPORT (OFF LINE)</text>
</svg>

</body>
</html>
```